IT Consulting, IT Beacon, Software Development, Network Solutions, Hosting

Attached is logo for our company, we just was the designers to come up with creative ideas to use the logo and the theme to come with creative and energetic business cards that leave an impression and stick in people's head.

Target Market(s)

Medical, Law, Entertainment, Real estate, any small to medium size business.

Industry/Entity Type

Business

Font styles to use
Serif
Sans Serif

```html
<!DOCTYPE html>
<html lang="en">
<head>
<meta charset="utf-8">
<title>IT Beacon – Business Card</title>
<link rel="stylesheet" href="https://fonts.googleapis.com/css2?family=Ubuntu:wght@400;500&family=Roboto+Condensed:wght@400&display=swap">
<style>
  :root {
    --stage: #dfe4e7;
    --label: #3a3a3a;
    --card: #333333;
    --gold-top: #dcbc58;
    --gold-bottom: #c9a43a;
    --gold-divider: rgba(255, 255, 255, 0.12);
    --icon-col: #9b9b9b;
    --icon-col-dark: #8d8d8d;
    --icon: #f2f2f2;
    --ink: #1f1f1f;
    --ink-soft: #fdf6e0;
    --brand: #f2c417;
    --band-light: #8a8a8a;
    --band-green: #5f6b3e;
  }
  * { margin: 0; padding: 0; box-sizing: border-box; }
  html, body { width: 1200px; height: 1000px; overflow: hidden; }
  body { background: var(--stage); position: relative; font-family: "Ubuntu", sans-serif; }

  .side-label {
    position: absolute; left: 0; width: 1200px; text-align: center;
    font-family: "Roboto Condensed", sans-serif; font-size: 38px; color: var(--label);
    letter-spacing: 0.5px;
  }
  .side-label--front { top: 16px; left: -5px; }
  .side-label--back { top: 490px; left: -13px; }

  .card {
    position: absolute; left: 230px; width: 743px; background: var(--card);
  }
  .card--front { top: 74px; height: 387px; }
  .card--back { top: 541px; height: 385px; }

  .brand-name {
    position: absolute; font-weight: 400; color: var(--brand);
    white-space: nowrap; letter-spacing: 1px; transform: translate(-50%, -50%);
  }
  .card--front .brand-name { left: 175px; top: 179px; font-size: 40px; }
  .card--back .brand-name { left: 378px; top: 149px; font-size: 52px; }

  .icon-column {
    position: absolute; left: 320px; top: 38px; width: 78px; height: 328px;
    background: var(--icon-col); border-right: 2px solid #b5b5b5;
  }
  .icon-cell {
    height: 78px; display: flex; align-items: center; justify-content: center;
    border-bottom: 1px solid var(--icon-col-dark);
  }
  .icon-cell svg { width: 34px; height: 34px; fill: var(--icon); }

  .info-panel {
    position: absolute; left: 400px; top: 43px; width: 304px; height: 317px;
  }
  .info-row {
    height: 78px; padding: 24px 0 0 18px;
    background: linear-gradient(var(--gold-top), var(--gold-bottom));
    border-bottom: 1px solid var(--gold-divider);
  }
  .info-row--contact, .info-row--social { padding-top: 17px; }
  .info-row--web { padding-top: 18px; }
  .info-row:last-child { height: 83px; }
  .info-title { font-size: 20px; font-weight: 500; color: var(--ink); line-height: 1; }
  .info-details { display: flex; margin-top: 6px; font-size: 12.5px; color: var(--ink-soft); line-height: 14px; }
  .info-item { display: flex; align-items: center; white-space: nowrap; }
  .info-item::before {
    content: ""; width: 0; height: 0; margin-right: 8px;
    border-left: 5px solid var(--ink); border-top: 4px solid transparent; border-bottom: 4px solid transparent;
  }
  .info-row--contact .info-item--second { margin-left: 62px; }
  .info-row--social .info-item--second { margin-left: 42px; }
  .info-row--web .info-details { margin-top: 8px; }

  .logo-band {
    position: absolute; left: 20px; top: 100px; width: 723px; height: 86px;
    background: linear-gradient(90deg, rgba(138,138,138,0) 0%, var(--band-light) 35%, var(--band-light) 65%, rgba(138,138,138,0) 100%);
  }
  .accent-band {
    position: absolute; left: 20px; top: 191px; width: 723px; height: 31px;
    background: linear-gradient(90deg, rgba(95,107,62,0) 0%, var(--band-green) 35%, var(--band-green) 70%, rgba(95,107,62,0) 100%);
  }
</style>
</head>
<body>
  <div class="side-label side-label--front">FRONT SIDE</div>

  <section class="card card--front">
    <div class="brand-name">IT BEACON</div>

    <div class="icon-column">
      <div class="icon-cell">
        <svg viewBox="0 0 34 34" aria-label="Person"><circle cx="17" cy="11" r="7"/><path d="M3 31c0-8 6-12 14-12s14 4 14 12z"/></svg>
      </div>
      <div class="icon-cell">
        <svg viewBox="0 0 34 34" aria-label="Envelope"><path d="M1 7h32v21H1z"/><path d="M1 7l16 13L33 7" fill="none" stroke="#9b9b9b" stroke-width="2"/></svg>
      </div>
      <div class="icon-cell">
        <svg viewBox="0 0 34 34" aria-label="Speech bubbles"><ellipse cx="14" cy="13" rx="13" ry="9"/><path d="M6 20l-3 7 9-5z"/><ellipse cx="22" cy="21" rx="10" ry="7"/><path d="M28 26l4 5-9-3z"/></svg>
      </div>
      <div class="icon-cell">
        <svg viewBox="0 0 34 34" aria-label="Cloud"><circle cx="19" cy="15" r="9"/><circle cx="9" cy="20" r="6"/><circle cx="27" cy="21" r="5"/><rect x="9" y="19" width="18" height="7"/></svg>
      </div>
    </div>

    <div class="info-panel">
      <div class="info-row info-row--name">
        <div class="info-title">Name Surname</div>
        <div class="info-details"><span class="info-item">Job Position</span></div>
      </div>
      <div class="info-row info-row--contact">
        <div class="info-title">Contact Me</div>
        <div class="info-details"><span class="info-item">01234567</span><span class="info-item info-item--second">youremail@email.com</span></div>
      </div>
      <div class="info-row info-row--social">
        <div class="info-title">Social</div>
        <div class="info-details"><span class="info-item">Chatterly</span><span class="info-item info-item--second">Pinglet</span></div>
      </div>
      <div class="info-row info-row--web">
        <div class="info-title">Web</div>
        <div class="info-details"><span class="info-item">www.yourwebsite.com</span></div>
      </div>
    </div>
  </section>

  <div class="side-label side-label--back">BACK SIDE</div>

  <section class="card card--back">
    <div class="logo-band"></div>
    <div class="accent-band"></div>
    <div class="brand-name">IT BEACON</div>
  </section>
</body>
</html>
```